KLR Values Puzzle Pieces

I want to use my logo (symbol only, not the words Marbel Vein Center) as the basis of the puzzle and incorporate our four values into the logo as four puzzle pieces. I want each puzzle piece to have one value on it and a line extending from the piece. At this point, I would like the bullet points of each value to be listed.
Here are the four values with the bullet points:
Cheese Movers
Are open to and embrace change, recognizing that it is a process, not a one-time event.
Are lifelong learners who continually use incremental improvements to enhance their knowledge and skills.
Possess grit, a combination of passion and perseverance, which allows them to overcome challenges and achieve their goals. Grit is the fuel to stay motivated and determined even when faced with obstacles or setbacks.
Are self-disciplined, working smart in thought and action by intentionally focusing on their goals.
Servant-Minded
Approaches work with humility, grace, and mercy, recognizing that serving others is a privilege.
Have a patient-centric approach, looking at the processes through the patient's eyes to ensure the best possible experience.
Educating patients with clarity and consistency, ensuring that they understand vein disease is a treatable but not curable condition.
The "Front Porch Rule" is a guiding principle that everyone is treated with respect, care, and compassion like our beloved family members.
We seek to provide vein care to all who need it.
Better Together
We emphasize the importance of having a team that rows in the same direction towards a common goal.
We have accountability and integrity by taking responsibility for our actions and their impact on others.
We are courageously real, speaking authentically to share thoughts and ideas while feeling valued for our unique perspectives.
We prioritize creating a supportive environment where team members feel they have the resources needed to succeed.
Balanced
We emphasize the importance of maintaining a work-life balance.
We are professional and take what we do seriously while still using laughter and fun to create a welcoming and friendly environment for patients and staff.
Valuable output is the greatest measure, not hours put in. Anyone can keep busy, but that does not equate to productivity.

```html
<!DOCTYPE html>
<html lang="en">
<head>
<meta charset="utf-8">
<title>KLR Values</title>
<link href="https://fonts.googleapis.com/css2?family=Roboto:wght@400;500;700&display=swap" rel="stylesheet">
<style>
  :root {
    --navy: #2b3178;
    --green: #128a44;
    --slate: #7b8796;
    --balanced-text: #80868d;
    --bg-center: #ffffff;
    --bg-edge: #d4d5d7;
    --hub: #e6e8ee;
  }
  * { box-sizing: border-box; margin: 0; padding: 0; }
  html, body { width: 1200px; height: 514px; overflow: hidden; }
  body {
    font-family: "Roboto", Arial, sans-serif;
    background: radial-gradient(ellipse 60% 75% at 50% 50%, var(--bg-center) 0%, #eeeeef 45%, var(--bg-edge) 100%);
    position: relative;
  }
  .connectors { position: absolute; left: 0; top: 0; }
  .value { position: absolute; }
  .value-title { font-size: 12.2px; font-weight: 700; line-height: 1; }
  .value-icon { display: block; margin: 6px 0 3px 1px; }
  .value-points { list-style: none; font-size: 10.2px; line-height: 12.7px; }
  .value-points li { position: relative; padding-left: 6px; text-align: justify; }
  .value-points li::before { content: "•"; position: absolute; left: -1px; top: 0; font-size: 9px; }
  .value--cheese { left: 49px; top: 66px; width: 180px; color: var(--navy); }
  .value--cheese .value-points { margin-left: 2px; }
  .value--together { left: 290px; top: 210px; width: 173px; color: var(--green); }
  .value--together .value-points { line-height: 12.35px; }
  .value--servant { left: 741px; top: 71px; width: 174px; color: var(--navy); }
  .value--balanced { left: 983px; top: 234px; width: 176px; color: var(--balanced-text); }
  .value--balanced .value-title { color: var(--balanced-text); }
  .value--balanced .value-points { font-size: 10px; line-height: 12.6px; margin-left: 2px; }
  .hub-name { font-family: "Roboto", Arial, sans-serif; font-weight: 700; font-size: 30px; fill: var(--navy); }
</style>
</head>
<body>

<svg class="connectors" width="1200" height="514" viewBox="0 0 1200 514" aria-hidden="true">
  <g fill="none" stroke-width="5.5" stroke-linejoin="miter">
    <polyline points="49,87 446,87 524,193" stroke="var(--navy)"/>
    <polyline points="851,92 729,92 652,200" stroke="var(--navy)"/>
    <polyline points="291,431 446,431 524,323" stroke="var(--green)"/>
    <polyline points="657,305 735,411 1155,411" stroke="var(--slate)"/>
  </g>
  <g fill="none" stroke-width="4.5">
    <path d="M504.2,227.6 A86,86 0 0 1 552.8,177.3" stroke="var(--navy)"/>
    <path d="M617.2,177.3 A86,86 0 0 1 665.8,227.6" stroke="var(--navy)"/>
    <path d="M665.8,286.4 A86,86 0 0 1 625.4,332.9" stroke="var(--slate)"/>
    <path d="M544.6,332.9 A86,86 0 0 1 504.2,286.4" stroke="var(--green)"/>
  </g>
  <circle cx="524" cy="193" r="5" fill="var(--navy)"/>
  <circle cx="652" cy="200" r="5" fill="var(--navy)"/>
  <circle cx="524" cy="323" r="5" fill="var(--green)"/>
  <circle cx="657" cy="305" r="5" fill="var(--slate)"/>

  <circle cx="585" cy="257" r="72" fill="var(--hub)"/>
  <text class="hub-name" x="585" y="268" text-anchor="middle">KLR</text>
</svg>

<section class="value value--cheese">
  <h2 class="value-title">Cheese Movers</h2>
  <svg class="value-icon" width="19" height="18" viewBox="0 0 19 18" aria-hidden="true">
    <g fill="var(--navy)">
      <circle cx="2.5" cy="2" r="2"/><circle cx="16.5" cy="2" r="2"/>
      <rect x="0.5" y="4.5" width="4" height="13"/><rect x="14.5" y="4.5" width="4" height="13"/>
      <rect x="4" y="4" width="11" height="5"/>
    </g>
  </svg>
  <ul class="value-points">
    <li>Are open to and embrace change, recognizing that it is a process, not a one-time event.</li>
    <li>Are lifelong learners who continually use incremental improvements to enhance their knowledge and skills.</li>
    <li>Possess grit, a combination of passion and perseverance, which allows them to overcome challenges and achieve their goals.Grit is the fuel to stay motivated and determined even when faced with obstacles or setbacks.</li>
    <li>Are self-disciplined, working smart in thought and action by intentionally focusing on their goals</li>
  </ul>
</section>

<section class="value value--together">
  <h2 class="value-title">Better Together</h2>
  <svg class="value-icon" width="18" height="16" viewBox="0 0 18 16" aria-hidden="true">
    <g fill="var(--green)">
      <circle cx="3" cy="2" r="2"/><circle cx="9" cy="2" r="2"/><circle cx="15" cy="2" r="2"/>
      <rect x="1.2" y="4.5" width="3.6" height="11"/><rect x="7.2" y="4.5" width="3.6" height="11"/><rect x="13.2" y="4.5" width="3.6" height="11"/>
    </g>
  </svg>
  <ul class="value-points">
    <li>We emphasize the importance of having a team that rows in the same direction towards a common goal.</li>
    <li>We have accountability and integrity by taking responsibility for our actions and their impact on others.</li>
    <li>We are courageously real, speaking authentically to share thoughts and ideas while feeling valued for our unique perspectives.</li>
    <li>We prioritize creating a supportive environment where team members feel they have the resources needed to succeed.</li>
  </ul>
</section>

<section class="value value--servant">
  <h2 class="value-title">Servant-Minded</h2>
  <svg class="value-icon" width="18" height="17" viewBox="0 0 18 17" aria-hidden="true">
    <g fill="none" stroke="var(--navy)" stroke-width="1.4">
      <path d="M3,12 A7.5,7.5 0 1 1 15,12"/>
    </g>
    <g fill="var(--navy)">
      <circle cx="9" cy="7" r="3"/>
      <path d="M3.5,17 Q9,8 14.5,17 Z"/>
    </g>
  </svg>
  <ul class="value-points">
    <li>Approaches work with humility, grace, and mercy, recognizing that serving others is a privilege.</li>
    <li>Have a patient-centric approach, looking at the processes through the patient's eyes to ensure the best possible experience.</li>
    <li>Educating patients with clarity and consistency, ensuring that they understand vein disease is a treatable but not curable condition.</li>
    <li>The "Front Porch Rule" is a guiding principle that everyone is treated with respect, care, and compassion like our beloved family members.</li>
    <li>We seek to provide vein care to all who need it.</li>
  </ul>
</section>

<section class="value value--balanced">
  <h2 class="value-title">Balanced</h2>
  <svg class="value-icon" width="19" height="14" viewBox="0 0 19 14" aria-hidden="true">
    <g fill="var(--balanced-text)">
      <circle cx="4" cy="3" r="3"/><circle cx="15" cy="3" r="3"/>
      <rect x="0" y="7" width="19" height="1.3"/>
      <path d="M9.5,8 L13,14 L6,14 Z"/>
    </g>
  </svg>
  <ul class="value-points">
    <li>We emphasize the importance of maintaining a work-life balance.</li>
    <li>We are professional and take what we do seriously while still using laughter and fun to create a welcoming and friendly environment for patients and staff.</li>
    <li>Valuable output is the greatest measure, not hours put in. Anyone can keep busy, but that does not equate to productivity.</li>
  </ul>
</section>

</body>
</html>
```